WordPress Site Design and Code for Technology Consulting Startup

We need a WordPress design and code to a new site on Nimbo Vault. We have the logo and colors ready. The site will be a brochure site with a CONTACT page that contains a form that the prospective client fills out. The other pages would be ABOUT / SERVICES (3 option drop-down) / SUPPORT. The site should be appropriate for an IT Consulting / IT Managed Services / IT Project Management services in the Chicago area.

Target Market(s)

Across small, medium, large businesses.

Industry/Entity Type

Technology, network infrastructure, IT.

Coding

Coded - Design and coding required

Number of Pages Required

5+ page

Requirements
Nice to have
• I prefer mid-modern / simple / art deco / minimalist.

```html
<!DOCTYPE html>
<html lang="en">
<head>
<meta charset="utf-8">
<title>Nimbo Vault – IT Project Management Services</title>
<link href="https://fonts.googleapis.com/css2?family=Montserrat:wght@400;500;600;700;800&display=swap" rel="stylesheet">
<style>
:root{
  --orange:#f37b1d;
  --orange-deep:#e0620c;
  --teal:#12899a;
  --teal-deep:#0c6470;
  --ink:#111418;
  --night:#0a0a0a;
  --navy:#1b2a48;
  --grey:#6d6f73;
  --line:#d7d9dc;
  --white:#ffffff;
}
*{box-sizing:border-box;margin:0;padding:0}
html,body{width:1200px;height:4580px;overflow:hidden}
body{font-family:"Montserrat",Arial,sans-serif;color:var(--ink);background:var(--white);position:relative}
.abs{position:absolute}
.btn{position:absolute;display:flex;align-items:center;justify-content:center;font-weight:700;font-size:14px;color:var(--white);border-radius:3px}
.btn-orange{background:var(--orange)}
.btn-teal{background:var(--teal)}
.btn-dark{background:var(--ink);border-bottom:3px solid var(--orange)}

/* header + hero */
.hero{position:absolute;left:0;top:0;width:1200px;height:560px;overflow:hidden}
.hero-photo{position:absolute;inset:0;background:linear-gradient(110deg,#0d3550 0%,#1d5f7a 30%,#3a6f88 50%,#b3642a 75%,#e2862f 100%)}
.hero-shade{position:absolute;inset:0;background:linear-gradient(180deg,rgba(5,15,30,.75) 0%,rgba(5,15,30,.25) 40%,rgba(5,15,30,.45) 100%)}
.topbar{position:absolute;left:0;top:0;width:1200px;height:40px;font-size:12px;color:#e6ecf0}
.topbar .item{position:absolute;top:12px;display:flex;align-items:center;gap:8px;white-space:nowrap}
.dot{width:12px;height:12px;border-radius:50%;background:var(--orange);display:inline-block}
.social{position:absolute;top:10px;display:flex;gap:10px;right:40px}
.social span{width:18px;height:18px;border-radius:50%;background:rgba(255,255,255,.8)}
.brand{position:absolute;display:flex;align-items:center;gap:8px;font-weight:800;font-size:18px;color:var(--white);letter-spacing:.5px;white-space:nowrap}
.brand i{width:22px;height:22px;background:var(--orange);display:block}
.nav{position:absolute;left:230px;top:56px;display:flex;gap:28px;font-size:16px;font-weight:600;color:var(--white);white-space:nowrap}
.call{position:absolute;left:820px;top:50px;display:flex;align-items:center;gap:12px;color:var(--white)}
.call .ico{width:34px;height:34px;border-radius:50%;background:var(--white);display:flex;align-items:center;justify-content:center}
.call small{display:block;font-size:11px;color:#cfd8de}
.call b{font-size:17px}
.hero-title{position:absolute;left:0;width:1200px;top:130px;text-align:center;font-size:64px;line-height:72px;font-weight:800;color:var(--white);letter-spacing:1px}
.hero-title .accent{color:var(--orange)}

/* about */
.about-deco{position:absolute}
.eyebrow{font-size:11px;font-weight:700;color:var(--orange);letter-spacing:1px}
.about-title{font-size:38px;line-height:46px;font-weight:800;color:var(--ink);white-space:nowrap}
.lead{font-size:14px;font-weight:700;color:var(--orange)}
.body{font-size:14px;line-height:21px;color:var(--grey)}
.feature{position:absolute;width:190px}
.feature h4{font-size:14px;font-weight:700;display:flex;gap:8px;align-items:center;margin-bottom:8px}
.feature h4 i{width:16px;height:16px;background:var(--orange);display:block;border:2px solid var(--navy)}
.photo{position:absolute}

/* services */
.services{position:absolute;left:0;top:1345px;width:1200px;height:840px;overflow:hidden}
.services-photo{position:absolute;inset:0;background:linear-gradient(120deg,#1d2a33 0%,#3b4650 40%,#6e5a45 70%,#9a6a3a 100%)}
.services-shade{position:absolute;inset:0;background:rgba(10,12,16,.55)}
.services-title{position:absolute;left:120px;top:95px;font-size:32px;line-height:40px;font-weight:800;color:var(--white)}
.services-title .accent{color:var(--orange)}
.card{position:absolute;top:230px;width:300px;height:520px;border:2px solid var(--white);background:rgba(20,22,26,.55)}
.card .pic{position:absolute;left:0;top:0;width:100%;height:220px}
.card h3{position:absolute;left:22px;top:250px;font-size:18px;font-weight:800;color:var(--white)}
.card p{position:absolute;left:22px;top:285px;width:250px;font-size:14px;line-height:21px;color:#d9dde1}

/* pricing */
.center{position:absolute;left:0;width:1200px;text-align:center}
.plan{position:absolute;background:var(--night);color:var(--white);text-align:center;border:3px solid var(--orange)}
.plan .tag{margin:0 auto;font-size:14px;font-weight:700}
.plan .price{font-size:48px;font-weight:800;color:var(--orange);margin-top:14px;line-height:60px}
.plan .price sup{font-size:22px;vertical-align:20px}
.plan h5{font-size:15px;font-weight:700;margin:8px 0 8px}
.plan ul{list-style:none;font-size:12px;line-height:24px;color:#d5d7da}

/* consult */
.consult-text{position:absolute;left:0;top:3205px;width:700px;height:350px;background:linear-gradient(90deg,var(--teal-deep),var(--teal))}

/* contact */
.field{position:absolute;height:36px;border:1px solid var(--line);font-size:12px;color:#9a9da1;padding:10px 12px}

/* footer */
.footer{position:absolute;left:0;top:4300px;width:1200px;height:280px;background:var(--night);color:var(--white)}
.footer h6{font-size:16px;font-weight:700;margin-bottom:18px}
.footer .col{position:absolute;top:50px;font-size:13px;line-height:22px;color:#c3c6ca}
.footer .col li{list-style:none}
</style>
</head>
<body>

<!-- HERO -->
<header class="hero">
  <div class="hero-photo" role="img" aria-label="Team working in a modern IT office, blue and orange tones"></div>
  <div class="hero-shade"></div>
  <div class="topbar">
    <div class="item" style="left:120px"><span class="dot"></span>hello@nimbovault.com</div>
    <div class="item" style="left:340px"><span class="dot"></span>42 Lakeside Ave, Chicago</div>
    <div class="item" style="left:870px">Help / Support / Contact</div>
    <div class="social"><span></span><span></span><span></span><span></span></div>
  </div>
  <div class="brand" style="left:24px;top:54px"><i></i>NIMBO VAULT</div>
  <nav class="nav"><span>Home</span><span>About</span><span>Services ▾</span><span>Contact</span></nav>
  <div class="call">
    <div class="ico"><svg width="16" height="16" viewBox="0 0 24 24"><path fill="#f37b1d" d="M6.6 10.8a15 15 0 0 0 6.6 6.6l2.2-2.2a1 1 0 0 1 1-.25 11 11 0 0 0 3.6.6 1 1 0 0 1 1 1V20a1 1 0 0 1-1 1A17 17 0 0 1 3 4a1 1 0 0 1 1-1h3.5a1 1 0 0 1 1 1c0 1.25.2 2.45.6 3.6a1 1 0 0 1-.25 1z"/></svg></div>
    <div><small>Call Anytime</small><b>+1 800 555 0190</b></div>
  </div>
  <h1 class="hero-title">IT PROJECT<br><span class="accent">MANAGEMENT</span><br>SERVICES</h1>
  <div class="btn btn-orange" style="left:460px;top:390px;width:130px;height:36px">Discover More</div>
  <div class="btn" style="left:610px;top:390px;width:130px;height:36px;background:#1a1d22">Get a quote</div>
</header>

<!-- ABOUT -->
<section>
  <svg class="about-deco" style="left:0;top:560px" width="1200" height="780" viewBox="0 0 1200 780">
    <polygon points="0,0 220,0 0,120" fill="#eceef0"/>
    <polygon points="1200,430 1200,620 1090,680" fill="#e4e6e9"/>
    <polygon points="0,700 640,720 1200,680 1200,780 0,780" fill="#f4f5f6"/>
    <rect x="700" y="170" width="12" height="180" fill="#1b2a48"/>
    <rect x="1108" y="400" width="10" height="200" fill="#c8cbcf"/>
  </svg>
  <div class="abs eyebrow" style="left:120px;top:610px">WELCOME TO NIMBO VAULT</div>
  <h2 class="abs about-title" style="left:120px;top:632px">Best IT Technology<br>Services you can Trust</h2>
  <div class="abs lead" style="left:120px;top:745px">The professional approach to Technology.</div>
  <p class="abs body" style="left:120px;top:775px;width:440px">It is a long established fact that a reader will be distracted by the readable content of a page when looking at its layout. The point of using Lorem Ipsum is that it has a more-or-less normal distribution of letters, as opposed to using Content here, content here, making it look like readable English.</p>
  <div class="feature" style="left:120px;top:915px"><h4><i></i>Project Management</h4><p class="body">It is a long established fact that a reader will be distracted.</p></div>
  <div class="feature" style="left:340px;top:915px"><h4><i></i>Project Framework</h4><p class="body">It is a long established fact that a reader will be distracted.</p></div>
  <div class="btn btn-dark" style="left:120px;top:1130px;width:110px;height:36px">See More</div>

  <div class="abs" style="left:690px;top:580px;width:390px;height:420px;background:var(--orange)"></div>
  <div class="abs" style="left:720px;top:600px;width:350px;height:420px;background:var(--white)"></div>
  <div class="photo" role="img" aria-label="Person exploring a virtual reality headset in a neon-lit room" style="left:740px;top:610px;width:320px;height:400px;background:linear-gradient(150deg,#2a1b5c 0%,#6b2f8f 40%,#1f4f8a 75%,#0f1c33 100%)"></div>
</section>

<!-- SERVICES -->
<section class="services">
  <div class="services-photo" role="img" aria-label="Open-plan office with staff at computer desks"></div>
  <div class="services-shade"></div>
  <h2 class="services-title">OUR<br><span class="accent">PROFESSIONAL</span><br>SERVICES</h2>
  <div class="btn btn-dark" style="left:940px;top:125px;width:110px;height:34px;border-bottom:0">See More</div>

  <article class="card" style="left:132px">
    <div class="pic" role="img" aria-label="Engineers reviewing a project board" style="background:linear-gradient(135deg,#4a3a32,#8a5a3c)"></div>
    <h3>PROJECT MANAGEMENT</h3>
    <p>It is a long established fact that a reader will be distracted by the readable content of a page when looking.</p>
    <div class="btn btn-teal" style="left:22px;top:440px;width:100px;height:32px">See More</div>
  </article>
  <article class="card" style="left:450px">
    <div class="pic" role="img" aria-label="Hands around a glowing plasma globe" style="background:radial-gradient(circle at 50% 55%,#b35cff 0%,#5a2fa0 35%,#1a1230 80%)"></div>
    <h3>PROJECT FRAMEWORK</h3>
    <p>It is a long established fact that a reader will be distracted by the readable content of a page when looking.</p>
    <div class="btn btn-teal" style="left:22px;top:440px;width:100px;height:32px">See More</div>
  </article>
  <article class="card" style="left:768px">
    <div class="pic" role="img" aria-label="Laptop showing control dashboards on a desk" style="background:linear-gradient(135deg,#cfd6dc,#7f97a8)"></div>
    <h3>PROJECT CONTROLING</h3>
    <p>It is a long established fact that a reader will be distracted by the readable content of a page when looking.</p>
    <div class="btn btn-teal" style="left:22px;top:440px;width:100px;height:32px">See More</div>
  </article>
</section>

<!-- PRICING -->
<section>
  <div class="center eyebrow" style="top:2318px;font-size:14px">PRICING PLANS</div>
  <h2 class="center" style="top:2345px;font-size:30px;font-weight:800">Our exciting <span style="color:var(--teal)">packages</span> that fulfill your need</h2>
  <p class="center body" style="top:2398px;left:300px;width:600px">We have fantastic and carefully bundled packages in store for you that are easy on your pocket and deliver huge value. In case you need a personalized package for your campaign, we can deliver that as well.</p>

  <div class="plan" style="left:132px;top:2530px;width:280px;height:400px;padding-top:20px">
    <div class="tag" style="background:var(--white);color:var(--ink);width:200px;padding:6px 0">Basic Combo Package</div>
    <div class="price"><sup>$</sup>195<sup>.99</sup></div>
    <h5>Logo Design</h5>
    <ul><li>2 Custom Logo Design Concepts</li><li>By 2 Designers</li><li>Icon Design</li><li>All Final File Formats</li><li>Business Stationery</li><li>Business Card, Letterhead</li></ul>
    <div class="btn btn-teal" style="left:87px;top:350px;width:100px;height:30px">See More</div>
  </div>

  <div class="plan" style="left:475px;top:2490px;width:250px;height:540px;border:0;background:var(--night)">
    <div class="tag" style="background:var(--teal);color:var(--white);width:230px;padding:7px 0;margin-top:10px">Pro Combo Package</div>
    <div class="price" style="color:var(--white)"><sup>$</sup>950<sup>.99</sup></div>
    <h5>Logo Design</h5>
    <ul><li>3 Custom Logo Design Concepts</li><li>By 3 Designers</li><li>Icon Design</li><li>All Final File Formats</li><li>Business Stationery</li><li>Business Card, Letterhead</li><li>Envelope, Fax Template</li><li>MS Word Letterhead</li><li>Website Design</li><li>Logo Design</li></ul>
    <div class="btn" style="left:75px;top:490px;width:100px;height:30px;border:1px solid var(--white);background:transparent">See More</div>
  </div>

  <div class="plan" style="left:788px;top:2530px;width:280px;height:400px;padding-top:20px">
    <div class="tag" style="background:var(--white);color:var(--ink);width:200px;padding:6px 0">Elite Combo Package</div>
    <div class="price"><sup>$</sup>250<sup>.99</sup></div>
    <h5>Logo Design</h5>
    <ul><li>4 Custom Logo Design Concepts</li><li>By 4 Designers</li><li>Icon Design</li><li>All Final File Formats</li><li>Business Stationery</li><li>Envelope, Fax Template</li></ul>
    <div class="btn btn-teal" style="left:87px;top:350px;width:100px;height:30px">See More</div>
  </div>
</section>

<!-- CONSULTATION -->
<section>
  <div class="abs" style="left:0;top:3205px;width:1200px;height:350px;background:#15171b"></div>
  <div class="consult-text"></div>
  <h2 class="abs" style="left:60px;top:3245px;width:560px;font-size:36px;line-height:44px;font-weight:800;color:var(--white);white-space:nowrap">Need It solution &amp;<br>services consultation?</h2>
  <p class="abs body" style="left:60px;top:3348px;width:440px;color:#e3f1f3">It is a long established fact that a reader will be distracted by the readable content of a page when looking it is a long established fact that a reader will be distracted by the readable content of a page when looking.</p>
  <div class="btn btn-orange" style="left:60px;top:3465px;width:120px;height:34px">Get Solution</div>
  <div class="abs" role="img" aria-label="White humanoid service robot on a dark background" style="left:700px;top:3195px;width:380px;height:370px;background:radial-gradient(circle at 45% 45%,#e8ecef 0%,#9aa3aa 30%,#2a2f35 70%,#15171b 100%)"></div>
</section>

<!-- CONTACT -->
<section>
  <svg class="abs" style="left:0;top:3590px" width="1200" height="700" viewBox="0 0 1200 700">
    <polygon points="200,20 330,20 330,560 200,600" fill="#f37b1d"/>
    <rect x="880" y="40" width="70" height="560" fill="#f37b1d"/>
    <rect x="360" y="650" width="10" height="50" fill="#c8cbcf"/>
    <rect x="955" y="80" width="12" height="200" fill="#c8cbcf"/>
  </svg>
  <div class="abs" style="left:225px;top:3620px;width:700px;height:640px;background:var(--white);border:3px solid var(--teal)"></div>
  <div class="center eyebrow" style="top:3650px">CONTACT</div>
  <h2 class="center" style="top:3668px;font-size:36px;font-weight:700">Get Connect with us</h2>
  <div class="field" style="left:300px;top:3735px;width:260px">Enter your first name</div>
  <div class="field" style="left:580px;top:3735px;width:260px">Enter your last name</div>
  <div class="field" style="left:300px;top:3790px;width:260px">Enter email address</div>
  <div class="field" style="left:580px;top:3790px;width:260px">Enter your Phone no</div>
  <div class="field" style="left:300px;top:3845px;width:540px;display:flex;justify-content:space-between">Please select the service you want <span style="color:var(--ink)">⌄</span></div>
  <div class="field" style="left:300px;top:3900px;width:540px;height:130px">Message.....</div>
  <div class="btn btn-teal" style="left:300px;top:4060px;width:100px;height:32px">Send</div>
</section>

<!-- FOOTER -->
<footer class="footer">
  <div class="col" style="left:130px;width:230px">
    <h6 style="color:var(--white)">Build with Nimbo Vault</h6>
    <p>It is a long established fact that a reader will be distracted by the readable content of a page when looking.</p>
    <p style="margin-top:14px;color:var(--white)">◷ 9am – 5pm EST<br>Sunday Closed</p>
  </div>
  <div class="col" style="left:440px"><h6 style="color:var(--white)">Menu</h6><ul><li>Home</li><li>About</li><li>Services</li><li>Contact</li></ul></div>
  <div class="col" style="left:580px"><h6 style="color:var(--white)">Our Services</h6><ul><li>Project Management</li><li>Project Framework</li><li>Monitoring &amp; Control</li></ul></div>
  <div class="col" style="left:810px"><h6 style="color:var(--white)">Office in NY</h6><ul><li>● 410 Harbor St</li><li>&nbsp;&nbsp;&nbsp;Brooklyn, NY 11201</li><li>● +1 212-555-0147</li><li>● +1 212-555-0148</li><li>● info@nimbovault.com</li><li>● care@nimbovault.com</li></ul></div>
  <div class="abs" style="left:0;top:228px;width:1200px;height:1px;background:#2a2c30"></div>
  <div class="brand" style="left:130px;top:244px;font-size:16px"><i style="width:18px;height:18px"></i>NIMBO VAULT</div>
  <div class="abs" style="left:700px;top:248px;font-size:12px;color:#a8abaf">© 2024 NIMBO VAULT All Rights Reserved</div>
</footer>

</body>
</html>
```